Flyer/Poster design required for volunteer activities

We need a STRIKING A4 Poster/Flyer advertising our conservation volunteer program activities which are currently happening in the area. This poster is to advertise the program once people have arrived on the island or to locals. The program covers 5 months, May-September 2019 and is focused on conservation. I have attached the following:
- a flyer which was previously created (QMR Habitat Helpers 2019 sm)to advertise the program - would prefer it has a similar striking resemblance, but not essential
- A mock up document 'HHQMR On Island Poster_2019_v2' with text -Logos-Images

Target Market(s)

Everyone interested in Environmental Adventure/Hiking/Citizen Science

Industry/Entity Type

Tourism

Font styles to use
Sans Serif

Requirements
Must have
• -A travel conservation focus
• -Must use 'QMR-Background Image' as the background to the design
• -The info of where to get more information and the social media details must be prominent

```html
<!DOCTYPE html>
<html lang="en">
<head>
<meta charset="utf-8">
<title>QMR Habitat Helpers 2019</title>
<link href="https://fonts.googleapis.com/css2?family=Arimo:wght@400;700&family=Open+Sans:wght@600;700;800&display=swap" rel="stylesheet">
<style>
:root{
  --sky:#dfeaf0;
  --sea-mid:#3f79a8;
  --sea-deep:#17447a;
  --title-blue:#1c6fc0;
  --yellow:#f7e01b;
  --tab-yellow:#f9dc5c;
  --tab-text:#1d4f9c;
  --red:#e3262b;
  --panel:rgba(20,45,80,.55);
  --band:rgba(25,30,40,.78);
  --tan:#c9a15a;
  --white:#ffffff;
}
*{margin:0;padding:0;box-sizing:border-box}
html,body{width:1200px;height:800px;overflow:hidden;background:#fff}
.poster{position:relative;width:1200px;height:800px;overflow:hidden;font-family:"Open Sans",Arial,sans-serif;color:var(--white)}
.backdrop{position:absolute;inset:0;background:
  radial-gradient(ellipse 420px 320px at 1080px 220px,#2f5a3e 0%,rgba(47,90,62,0) 70%),
  linear-gradient(180deg,var(--sky) 0%,#b9d0de 14%,var(--sea-mid) 30%,#245c92 55%,var(--sea-deep) 100%)}
.title{position:absolute;left:92px;top:72px;font-family:"Arimo",Arial,sans-serif;font-weight:700;font-size:31px;line-height:40px;color:var(--title-blue);text-align:center;width:420px}
.brand-mark{position:absolute;left:520px;top:70px;display:flex;align-items:center;gap:8px;font-family:"Arimo",Arial,sans-serif;font-weight:700;font-size:17px;color:var(--title-blue)}
.brand-mark .dot{width:18px;height:18px;border-radius:50%;background:var(--title-blue)}
.burst{position:absolute;left:745px;top:8px;width:270px;height:190px}
.burst-text{position:absolute;left:745px;top:60px;width:270px;text-align:center;font-family:"Arimo",Arial,sans-serif;font-weight:700;color:#fff}
.burst-text .months{font-size:25px;line-height:28px}
.burst-text .year{font-size:70px;line-height:72px}
.callout{position:absolute;left:0;top:197px;width:627px;height:56px;background:var(--band);padding:4px 0 0 10px;font-family:"Open Sans",Arial,sans-serif;font-weight:800;font-size:19.5px;line-height:23px;color:var(--yellow)}
.programme{position:absolute;left:0;top:267px;width:1200px;height:533px;background:var(--panel)}
.month-card{position:absolute;border:4px solid var(--yellow)}
.tab{position:absolute;top:-4px;right:-4px;background:var(--tab-yellow);color:var(--tab-text);text-align:center;font-family:"Arimo",Arial,sans-serif;font-weight:700;padding:3px 8px 3px}
.tab .month{font-size:19px;line-height:21px}
.tab .feature{font-size:13px;line-height:15px}
.photo{position:absolute}
.activities{position:absolute;font-weight:700;font-size:12.2px;line-height:19px;color:var(--white)}
.activities h3{font-size:12.2px;font-weight:800;text-transform:uppercase}
.card-may{left:24px;top:276px;width:589px;height:164px}
.card-june{left:24px;top:449px;width:589px;height:162px}
.card-july{left:24px;top:620px;width:589px;height:169px}
.card-aug{left:623px;top:451px;width:564px;height:160px}
.card-protect{left:623px;top:620px;width:564px;height:169px}
.info{position:absolute;left:623px;top:298px;width:540px;font-weight:700;font-size:15px;line-height:22px}
.info .follow{color:var(--yellow);font-weight:800}
.social{position:absolute;left:623px;width:430px;height:36px;display:flex;align-items:center;gap:10px;padding-left:8px;font-family:"Arimo",Arial,sans-serif;font-weight:700;font-size:22px;color:#fff}
.social-feed{top:367px;background:rgba(40,80,140,.85)}
.social-photo{top:404px;background:var(--tan)}
.social .icon{width:26px;height:26px;border-radius:50%;background:#fff}
.social-photo .icon{border-radius:6px}
</style>
</head>
<body>
<div class="poster">
  <div class="backdrop" role="img" aria-label="Aerial coastal view of the island with blue sea, headland and green mountains"></div>

  <h1 class="title">QUELL MARA ISLAND<br>QMR HABITAT HELPERS</h1>
  <div class="brand-mark"><span class="dot"></span>HHQMR</div>

  <svg class="burst" viewBox="0 0 270 190" aria-hidden="true">
    <polygon fill="#e3262b" points="135,4 152,28 178,12 184,40 214,32 208,60 240,62 224,88 256,100 226,118 246,144 214,148 220,178 190,168 178,188 156,172 135,186 114,172 92,188 80,168 50,178 56,148 24,144 44,118 14,100 46,88 30,62 62,60 56,32 86,40 92,12 118,28"/>
  </svg>
  <div class="burst-text"><div class="months">MAY - SEPTEMBER</div><div class="year">2019</div></div>

  <div class="callout">BE INVOLED IN PRESERVING PARADISE<br>JOIN THE QMR HABITAT HELPERS PROGRAM 2019</div>

  <div class="programme"></div>

  <section class="month-card card-may">
    <div class="tab" style="width:198px"><div class="month">MAY 2019</div><div class="feature">Feature Week: 19th – 26th May</div></div>
    <div class="photo" role="img" aria-label="Photo of a seabird resting on rocks" style="left:5px;top:29px;width:94px;height:91px;background:linear-gradient(160deg,#8a8f86,#4d5048)"></div>
    <div class="activities" style="left:100px;top:26px">
      <h3>Birds of Quell Mara Island</h3>
      -Ocean bird watching boat trips<br>
      -Guided tours of Woodhen and Currawong quarters<br>
      -Weekly lectures at the Quell Mara Museum<br>
      -Weekly screenings of documentaries on Bird and Island Conservation projects<br>
      -Self guided land bird survey tours
    </div>
  </section>

  <section class="month-card card-june">
    <div class="tab" style="width:220px"><div class="month">JUNE 2019</div><div class="feature">Feature Week: 3rd – 9th June</div></div>
    <div class="photo" role="img" aria-label="Underwater photo of a snorkeller recording marine data" style="left:5px;top:11px;width:107px;height:126px;background:linear-gradient(180deg,#4fb6d8,#1b6a9a)"></div>
    <div class="activities" style="left:115px;top:24px">
      <h3>Quell Mara Marine Park</h3>
      -Marine pest monitoring with marine park staff<br>
      -Marine plastic &amp; debris clean up activities<br>
      -Screenings of marine conservation documentaries at the museum<br>
      -Weekly lectures on Marine Life at the Quell Mara Museum<br>
      -Marine Activities with local operators
    </div>
  </section>

  <section class="month-card card-july">
    <div class="tab" style="width:230px"><div class="month">JULY 2019</div><div class="feature">Feature Week: 21st – 28th July</div></div>
    <div class="photo" role="img" aria-label="Photo of a walker on a forest trail" style="left:12px;top:24px;width:80px;height:124px;background:linear-gradient(180deg,#6e7a3c,#2d3a1c)"></div>
    <div class="activities" style="left:95px;top:28px;font-size:11.5px;line-height:17.5px">
      <h3 style="font-size:11.5px">Invasive Species</h3>
      -Guided walks to learn about the weed eradication program<br>
      -Weekly lectures on plants of Quell Mara Island<br>
      -Weekly screenings of documentaries on plant and island conservation projects<br>
      -Guided walks to Mount Harrow<br>
      -Local tour guides include commentaries on island plants
    </div>
  </section>

  <div class="info">
    See the QMR visitor centre for more information about<br>the QMR Habitat Helpers program for 2019<br>
    <span class="follow">FOLLOW US!</span>
  </div>
  <div class="social social-feed"><span class="icon"></span>www.friendsfeed.com</div>
  <div class="social social-photo"><span class="icon"></span>hhqmrphotos@hhqmr</div>

  <section class="month-card card-aug">
    <div class="tab" style="width:230px"><div class="month">AUGUST 2019</div><div class="feature">Feature Week: 11th – 19th August</div></div>
    <div class="photo" role="img" aria-label="Photo of a hand holding a stick insect" style="left:11px;top:29px;width:109px;height:76px;background:linear-gradient(135deg,#c8a08a,#5a4a42)"></div>
    <div class="activities" style="left:122px;top:30px;font-size:11.5px;line-height:18px">
      <h3 style="font-size:11.5px">Amazing Invertebrates</h3>
      -Guided night walks to learn about the island’s invertebrates<br>
      -Weekly viewing and presentation of the Quell Mara Phasmid<br>
      -Weekly lectures on invertebrates of Quell Mara Island at the museum<br>
      -Weekly screenings of documentaries on island conservation projects
    </div>
  </section>

  <section class="month-card card-protect">
    <div class="photo" role="img" aria-label="Map of the island and surrounding marine park" style="left:5px;top:30px;width:120px;height:106px;background:linear-gradient(135deg,#bfe6f2,#6fc2df)"></div>
    <div class="activities" style="left:130px;top:22px;font-size:11.5px;line-height:17.5px">
      <h3 style="font-size:11.5px">Protecting Paradise</h3>
      -Observational snorkel surveys with Marine Ecologists,<br>
      to assess populations of Mara’s<br>
      Anemonefish and other unique fish species<br>
      -Guided snorkel and glass bottom boat tour to assess coral health within the<br>
      Quell Mara Marine Park<br>
      -Guided walks to learn about the island’s conservation history
    </div>
  </section>
</div>
</body>
</html>
```